Real estate agent website

I am a new real estate agent and in of a simple but powerful website that is linked to the local Multiple listing services (MLS). It should have a lending page that is connected to my customer relationship management (CRM) software. It must have an ability for potential customers to search for properties and be able to communicate with me easily.
Updates

Updates: The website themes must includes MLS-IDX integration with a grid layout and property slider so i can showcase featured properties. I also would like to have future where potential client can search and have alerts depending on a search criteria.

Industry/Entity Type

Real Estate

Coding

Coded - Design and coding required

Number of Pages Required

3 page

Requirements
Must have
• Home page, Resources page, About Me with contact me window page

```html
<!DOCTYPE html>
<html lang="en">
<head>
<meta charset="utf-8">
<meta name="format-detection" content="telephone=no">
<title>Homekey Realty – Find Your Dream House</title>
<link rel="stylesheet" href="https://fonts.googleapis.com/css2?family=Montserrat:wght@400;500;600;700&family=Barlow:wght@400;500&display=swap">
<style>
:root{
  --navy:#0c2796;
  --blue:#3a3bb0;
  --violet:#3b2fb8;
  --red:#f20505;
  --grey:#ececec;
  --ink:#1b1b1b;
  --dark:#232224;
  --white:#ffffff;
  --muted:#8a8a8a;
}
*{box-sizing:border-box;margin:0;padding:0}
html,body{width:1200px;height:3027px;overflow:hidden}
body{position:relative;background:var(--white);font-family:"Montserrat",sans-serif;color:var(--ink)}
a{color:inherit;text-decoration:none}
.abs{position:absolute}

/* hero */
.hero{left:0;top:0;width:1200px;height:600px}
.hero-bg{left:0;top:0;width:1200px;height:600px}
.brand{left:129px;top:18px;display:flex;align-items:center;gap:10px;color:var(--white);font-weight:700;font-size:22px}
.brand-mark{width:30px;height:30px;background:var(--white);border-radius:6px}
.nav{top:36px;font-size:17px;font-weight:500;color:var(--white)}
.nav-about{left:535px}.nav-property{left:640px}.nav-contact{left:766px}
.phone{left:884px;top:31px;display:flex;align-items:center;gap:10px;color:var(--white);font-size:17px;font-weight:500}
.phone-icon{width:38px;height:38px;border-radius:50%;background:var(--white);display:flex;align-items:center;justify-content:center}
.hero-title{left:129px;top:197px;font-size:44px;line-height:46px;font-weight:600;color:var(--white)}
.hero-lead{left:129px;top:302px;width:420px;font-size:17.5px;line-height:26px;color:var(--white)}
.hero-btn{left:129px;top:382px;width:172px;height:44px;border-radius:10px;background:var(--violet);color:var(--white);font-size:14px;font-weight:600;display:flex;align-items:center;justify-content:center;gap:10px}
.agent-photo{left:588px;top:88px;width:393px;height:488px;border-radius:180px 180px 20px 20px;background:linear-gradient(180deg,#3b3f5a 0%,#1c1d26 70%,#15161c 100%)}

/* featured */
.section-title{left:0;width:1200px;text-align:center;top:676px;font-size:29px;font-weight:600}
.card{width:265px;height:381px;background:var(--white);box-shadow:0 2px 10px rgba(0,0,0,.12)}
.card-photo{position:absolute;left:0;top:0;width:265px;height:166px}
.photo-a{background:linear-gradient(180deg,#9db8d8 0%,#c9bfb0 50%,#4f7a35 100%)}
.photo-b{background:linear-gradient(180deg,#7fa6cf 0%,#d9d9d2 55%,#496f2e 100%)}
.photo-c{background:linear-gradient(180deg,#8fb5e0 0%,#8a5a44 55%,#3f6a28 100%)}
.photo-d{background:linear-gradient(180deg,#b9c8d8 0%,#e8e6e2 55%,#444a44 100%)}
.photo-e{background:linear-gradient(180deg,#6f9ed2 0%,#d7e0ea 55%,#5a6270 100%)}
.badge{position:absolute;right:22px;top:16px;height:22px;padding:0 12px;border-radius:11px;background:var(--red);color:var(--white);font-size:13px;line-height:22px;font-weight:500}
.card-title{position:absolute;left:15px;top:183px;font-size:17px;font-weight:500;white-space:nowrap}
.card-price{position:absolute;left:18px;top:215px;font-size:19px;font-weight:500;color:var(--red)}
.card-loc{position:absolute;left:15px;top:249px;font-size:11.5px}
.card-specs{position:absolute;left:18px;top:277px;display:flex;gap:14px;font-size:11px;align-items:center}
.spec{display:flex;align-items:center;gap:6px}
.card-btn{position:absolute;left:19px;top:310px;width:203px;height:45px;border-radius:9px;background:var(--violet);color:var(--white);font-size:14px;font-weight:500;display:flex;align-items:center;justify-content:center}

/* about + contact bands */
.bands{left:0;top:1660px;width:1200px;height:1166px}
.about-photo{left:194px;top:1675px;width:358px;height:540px;border-radius:160px 160px 0 0;background:linear-gradient(180deg,#5a4a44 0%,#4a4a4e 40%,#2f3034 100%)}
.about-title{left:650px;top:1796px;font-size:28px;font-weight:600}
.about-text{left:650px;top:1851px;width:440px;font-size:13.2px;line-height:24.2px}

.contact-title{left:0;width:1200px;text-align:center;top:2312px;font-size:28px;font-weight:600;color:var(--white)}
.field{background:var(--white);font-family:"Barlow",sans-serif;font-size:12.5px;color:var(--muted);padding:18px 0 0 18px}
.f-first{left:282px;top:2376px;width:311px;height:48px}
.f-last{left:607px;top:2376px;width:312px;height:48px}
.f-email{left:282px;top:2437px;width:311px;height:48px}
.f-phone{left:607px;top:2437px;width:312px;height:48px}
.f-msg{left:282px;top:2517px;width:637px;height:139px;padding-top:18px}
.submit{left:280px;top:2673px;width:137px;height:39px;border-radius:20px;background:#3a3a3a;color:var(--white);font-size:14px;font-weight:500;display:flex;align-items:center;justify-content:center}

/* footer */
.footer{left:0;top:2826px;width:1200px;height:201px;background:var(--dark)}
.footer-brand{left:134px;top:2871px;width:81px;height:81px;background:var(--white);display:flex;align-items:center;justify-content:center;color:var(--blue);font-weight:700;font-size:13px}
.footer-info{left:468px;top:2880px;color:var(--white);font-family:"Barlow",sans-serif;font-size:14px}
.footer-info li{list-style:none;display:flex;align-items:center;gap:12px;height:29.5px;color:var(--white)}
.connect{left:864px;top:2888px;color:var(--white);font-family:"Barlow",sans-serif;font-size:16px;font-weight:500}
.socials{left:866px;top:2925px;display:flex;gap:15px}
.social{width:20px;height:20px;border-radius:50%;background:var(--white)}
.copyright{left:868px;top:2965px;color:var(--white);font-family:"Barlow",sans-serif;font-size:11px}
</style>
</head>
<body>

<header class="abs hero">
  <svg class="abs hero-bg" width="1200" height="600" viewBox="0 0 1200 600">
    <defs>
      <linearGradient id="heroFill" x1="0" y1="0" x2="0" y2="1">
        <stop offset="0" stop-color="#0b2494"/>
        <stop offset=".35" stop-color="#3c3fb0"/>
        <stop offset="1" stop-color="#5556b5"/>
      </linearGradient>
    </defs>
    <path d="M0 0H1200V546Q900 565 600 600Q300 565 0 546Z" fill="var(--red)"/>
    <path d="M0 0H1200V541Q900 560 600 585Q300 560 0 541Z" fill="url(#heroFill)"/>
  </svg>
  <div class="abs agent-photo" role="img" aria-label="Portrait of a smiling real estate agent in a dark suit with arms crossed"></div>

  <div class="abs brand"><span class="brand-mark"></span>Homekey</div>
  <a class="abs nav nav-about">About</a>
  <a class="abs nav nav-property">Property</a>
  <a class="abs nav nav-contact">Contact</a>
  <div class="abs phone">
    <span class="phone-icon"><svg width="18" height="18" viewBox="0 0 24 24"><path d="M5 3h4l2 5-2.5 1.5a11 11 0 0 0 6 6L16 13l5 2v4a2 2 0 0 1-2 2A16 16 0 0 1 3 5a2 2 0 0 1 2-2z" fill="none" stroke="#1b1b1b" stroke-width="1.6" stroke-linejoin="round"/></svg></span>
    +62 555 01 23
  </div>

  <h1 class="abs hero-title">Find Your Dream<br>House</h1>
  <p class="abs hero-lead">Lorem ipsum dolor sit amet consectetur. Est adipiscing euismod id tincidunt at mi nibh.</p>
  <a class="abs hero-btn">Find property
    <svg width="18" height="18" viewBox="0 0 24 24"><path d="M3 11L12 3l9 8v10h-6v-6H9v6H3z" fill="none" stroke="#fff" stroke-width="1.8" stroke-linejoin="round"/></svg>
  </a>
</header>

<h2 class="abs section-title">Feautured Property</h2>

<article class="abs card" style="left:157px;top:751px">
  <div class="card-photo photo-a" role="img" aria-label="Single-storey house with gabled porch and green lawn"></div>
  <span class="badge">HOUSE</span>
  <h3 class="card-title">Mini House two Floor MT</h3>
  <p class="card-price">$345,842</p>
  <p class="card-loc">Cakung, DKI Jakarta</p>
  <div class="card-specs"><span class="spec"><svg width="12" height="9"><rect x="0" y="3" width="12" height="4" fill="#333"/><rect x="1" y="0" width="4" height="3" fill="#333"/></svg>2</span><span class="spec"><svg width="12" height="9"><rect x="0" y="4" width="12" height="5" rx="1" fill="#333"/><rect x="1" y="0" width="2" height="4" fill="#333"/></svg>1</span><span class="spec"><svg width="12" height="9"><rect x="0" y="3" width="12" height="5" rx="2" fill="#333"/><rect x="2" y="0" width="8" height="3" fill="#333"/></svg>2</span><span class="spec"><svg width="12" height="12"><path d="M1 0v11h11" fill="none" stroke="#333" stroke-width="2"/></svg>1472 sqft</span></div>
  <a class="card-btn">DETAILS</a>
</article>

<article class="abs card" style="left:462px;top:751px">
  <div class="card-photo photo-b" role="img" aria-label="White farmhouse with dark roof among tall trees"></div>
  <span class="badge" style="right:96px">HOUSE</span>
  <h3 class="card-title">Mini House two Floor MT</h3>
  <p class="card-price">$345,842</p>
  <p class="card-loc">Cakung, DKI Jakarta</p>
  <div class="card-specs"><span class="spec"><svg width="12" height="9"><rect x="0" y="3" width="12" height="4" fill="#333"/><rect x="1" y="0" width="4" height="3" fill="#333"/></svg>2</span><span class="spec"><svg width="12" height="9"><rect x="0" y="4" width="12" height="5" rx="1" fill="#333"/><rect x="1" y="0" width="2" height="4" fill="#333"/></svg>1</span><span class="spec"><svg width="12" height="9"><rect x="0" y="3" width="12" height="5" rx="2" fill="#333"/><rect x="2" y="0" width="8" height="3" fill="#333"/></svg>2</span><span class="spec"><svg width="12" height="12"><path d="M1 0v11h11" fill="none" stroke="#333" stroke-width="2"/></svg>1472 sqft</span></div>
  <a class="card-btn" style="left:31px">DETAILS</a>
</article>

<article class="abs card" style="left:765px;top:751px">
  <div class="card-photo photo-c" role="img" aria-label="Brick two-storey family house with lawn"></div>
  <span class="badge">HOUSE</span>
  <h3 class="card-title">Mini House two Floor MT</h3>
  <p class="card-price">$345,842</p>
  <p class="card-loc">Cakung, DKI Jakarta</p>
  <div class="card-specs"><span class="spec"><svg width="12" height="9"><rect x="0" y="3" width="12" height="4" fill="#333"/><rect x="1" y="0" width="4" height="3" fill="#333"/></svg>2</span><span class="spec"><svg width="12" height="9"><rect x="0" y="4" width="12" height="5" rx="1" fill="#333"/><rect x="1" y="0" width="2" height="4" fill="#333"/></svg>1</span><span class="spec"><svg width="12" height="9"><rect x="0" y="3" width="12" height="5" rx="2" fill="#333"/><rect x="2" y="0" width="8" height="3" fill="#333"/></svg>2</span><span class="spec"><svg width="12" height="12"><path d="M1 0v11h11" fill="none" stroke="#333" stroke-width="2"/></svg>1472 sqft</span></div>
  <a class="card-btn">DETAILS</a>
</article>

<article class="abs card" style="left:163px;top:1166px">
  <div class="card-photo photo-d" role="img" aria-label="Modern white villa with glass balconies at dusk"></div>
  <span class="badge">HOUSE</span>
  <h3 class="card-title">Mini House two Floor MT</h3>
  <p class="card-price">$345,842</p>
  <p class="card-loc">Cakung, DKI Jakarta</p>
  <div class="card-specs"><span class="spec"><svg width="12" height="9"><rect x="0" y="3" width="12" height="4" fill="#333"/><rect x="1" y="0" width="4" height="3" fill="#333"/></svg>2</span><span class="spec"><svg width="12" height="9"><rect x="0" y="4" width="12" height="5" rx="1" fill="#333"/><rect x="1" y="0" width="2" height="4" fill="#333"/></svg>1</span><span class="spec"><svg width="12" height="9"><rect x="0" y="3" width="12" height="5" rx="2" fill="#333"/><rect x="2" y="0" width="8" height="3" fill="#333"/></svg>2</span><span class="spec"><svg width="12" height="12"><path d="M1 0v11h11" fill="none" stroke="#333" stroke-width="2"/></svg>1472 sqft</span></div>
  <a class="card-btn">DETAILS</a>
</article>

<article class="abs card" style="left:468px;top:1166px">
  <div class="card-photo photo-e" role="img" aria-label="Minimalist modern house with carport under evening sky"></div>
  <span class="badge" style="right:96px">HOUSE</span>
  <h3 class="card-title">Mini House two Floor MT</h3>
  <p class="card-price">$345,842</p>
  <p class="card-loc" style="left:76px">Cakung, DKI Jakarta</p>
  <div class="card-specs" style="left:36px"><span class="spec"><svg width="12" height="9"><rect x="0" y="3" width="12" height="4" fill="#333"/><rect x="1" y="0" width="4" height="3" fill="#333"/></svg>2</span><span class="spec"><svg width="12" height="9"><rect x="0" y="4" width="12" height="5" rx="1" fill="#333"/><rect x="1" y="0" width="2" height="4" fill="#333"/></svg>1</span><span class="spec"><svg width="12" height="9"><rect x="0" y="3" width="12" height="5" rx="2" fill="#333"/><rect x="2" y="0" width="8" height="3" fill="#333"/></svg>2</span><span class="spec"><svg width="12" height="12"><path d="M1 0v11h11" fill="none" stroke="#333" stroke-width="2"/></svg>1472 sqft</span></div>
  <a class="card-btn" style="left:31px">DETAILS</a>
</article>

<article class="abs card" style="left:771px;top:1166px">
  <div class="card-photo photo-a" role="img" aria-label="Single-storey house with gabled porch and green lawn"></div>
  <span class="badge">HOUSE</span>
  <h3 class="card-title">Mini House two Floor MT</h3>
  <p class="card-price">$345,842</p>
  <p class="card-loc">Cakung, DKI Jakarta</p>
  <div class="card-specs"><span class="spec"><svg width="12" height="9"><rect x="0" y="3" width="12" height="4" fill="#333"/><rect x="1" y="0" width="4" height="3" fill="#333"/></svg>2</span><span class="spec"><svg width="12" height="9"><rect x="0" y="4" width="12" height="5" rx="1" fill="#333"/><rect x="1" y="0" width="2" height="4" fill="#333"/></svg>1</span><span class="spec"><svg width="12" height="9"><rect x="0" y="3" width="12" height="5" rx="2" fill="#333"/><rect x="2" y="0" width="8" height="3" fill="#333"/></svg>2</span><span class="spec"><svg width="12" height="12"><path d="M1 0v11h11" fill="none" stroke="#333" stroke-width="2"/></svg>1472 sqft</span></div>
  <a class="card-btn">DETAILS</a>
</article>

<svg class="abs bands" width="1200" height="1166" viewBox="0 0 1200 1166">
  <path d="M0 97L1200 15V1166H0Z" fill="var(--grey)"/>
  <path d="M0 573L1200 488V1166H0Z" fill="var(--red)"/>
</svg>
<div class="abs about-photo" role="img" aria-label="Smiling agent in a grey suit and red tie offering a handshake"></div>
<h2 class="abs about-title">ABOUT ME</h2>
<p class="abs about-text">Lorem ipsum dolor sit amet consectetur. Diam amet lacinia sed elit sed consectetur magna auctor. Sit imperdiet pellentesque maecenas ornare massa. Eu phasellus tincidunt cras ornare augue. Nulla in dignissim urna sit placerat lectus ut adipiscing. Id dui quam pellentesque nunc. Elit tristique volutpat lectus aenean. Aenean at id nisl morbi mauris urna. Amet scelerisque purus velit libero tellus sagittis sit nulla id. Ultrices amet proin risus ullamcorper. Elementum sem tortor dolor sed. Nec magna tortor posuere id libero neque.</p>

<h2 class="abs contact-title">CONTACT US</h2>
<div class="abs field f-first">First name</div>
<div class="abs field f-last">Last name</div>
<div class="abs field f-email">Email Address</div>
<div class="abs field f-phone">Phone number</div>
<div class="abs field f-msg">Message</div>
<a class="abs submit">Submit</a>

<footer class="abs footer"></footer>
<div class="abs footer-brand">Homekey</div>
<ul class="abs footer-info">
  <li><svg width="16" height="18" viewBox="0 0 16 18"><path d="M8 17s6-6 6-10A6 6 0 0 0 2 7c0 4 6 10 6 10z" fill="none" stroke="#fff" stroke-width="1.4"/><circle cx="8" cy="7" r="2" fill="none" stroke="#fff" stroke-width="1.4"/></svg><span>Your location here</span></li>
  <li><svg width="18" height="14" viewBox="0 0 18 14"><rect x="1" y="1" width="16" height="12" fill="none" stroke="#fff" stroke-width="1.4"/><path d="M1 1l8 7 8-7" fill="none" stroke="#fff" stroke-width="1.4"/></svg><span>hello@homekeyrealty.com</span></li>
  <li><svg width="16" height="16" viewBox="0 0 24 24"><path d="M5 3h4l2 5-2.5 1.5a11 11 0 0 0 6 6L16 13l5 2v4a2 2 0 0 1-2 2A16 16 0 0 1 3 5a2 2 0 0 1 2-2z" fill="none" stroke="#fff" stroke-width="1.8"/></svg><span>000 555 010</span></li>
</ul>
<p class="abs connect">CONNECTED WITH US</p>
<div class="abs socials" aria-label="Social links">
  <span class="social"></span><span class="social"></span><span class="social"></span><span class="social"></span><span class="social"></span>
</div>
<p class="abs copyright">©2022 Homekey Realty. All rights reserved.</p>

</body>
</html>
```